Business card design needed

Black on pure white.
Two coloured logos.
Text/info on back

Industry/Entity Type

Business

Contact Information for Business Card

Swiftgate Portals Pty. Ltd.
Varnel Corvista High Speed Doors.
Gordon T. Halloway
0491 538260
sales@swiftgateportals.com.au
www.swiftgateportals.com.au

Logo styles of interest
Abstract Logo

```html
<!DOCTYPE html>
<html lang="en">
<head>
<meta charset="utf-8">
<title>Swiftgate Portals – Business Card</title>
<link rel="stylesheet" href="https://fonts.googleapis.com/css2?family=Source+Sans+3:wght@300;400;600&display=swap">
<style>
  :root {
    --backdrop: #e4e4e4;
    --ink: #111111;
    --paper: #ffffff;
    --card-black: #121212;
    --reverse-ink: #f4f4f4;
  }
  * { box-sizing: border-box; margin: 0; padding: 0; }
  html, body {
    width: 1200px; height: 900px; overflow: hidden;
    background: var(--backdrop);
    font-family: "Source Sans 3", sans-serif;
  }
  .stage { position: relative; width: 1200px; height: 900px; }

  .card {
    position: absolute; top: 180px;
    width: 330px; height: 540px;
    box-shadow: 0 6px 18px rgba(0,0,0,.18);
    overflow: hidden;
  }

  /* Front: black */
  .card--front { left: 225px; background: var(--card-black); color: var(--reverse-ink); }
  .front__company {
    position: absolute; left: 40px; bottom: 40px;
    writing-mode: vertical-rl; transform: rotate(180deg);
    font-size: 21px; font-weight: 400; letter-spacing: .3px; white-space: nowrap;
  }
  .front__logo-box {
    position: absolute; left: 132px; top: 190px;
    width: 140px; height: 140px;
    border: 3px solid var(--reverse-ink);
    display: flex; align-items: center; justify-content: center;
  }
  .front__logo-text {
    writing-mode: vertical-rl; transform: rotate(180deg);
    font-size: 30px; font-weight: 400; line-height: 1.05; text-align: left;
  }
  .front__brand-line {
    position: absolute; right: 20px; top: 22px;
    writing-mode: vertical-rl; transform: rotate(180deg);
    font-size: 8px; letter-spacing: .4px; opacity: .8; white-space: nowrap;
  }

  /* Back: white, content set landscape and turned */
  .card--back { left: 645px; background: var(--paper); color: var(--ink); }
  .back__layout {
    position: absolute; left: 50%; top: 50%;
    width: 540px; height: 330px;
    transform: translate(-50%, -50%) rotate(-90deg);
    display: flex; align-items: center; gap: 20px;
    padding: 0 28px;
  }
  .name-block {
    border: 3px solid var(--ink);
    padding: 12px 16px 10px;
    text-align: left;
    flex: none;
  }
  .name-block__first { font-size: 26px; font-weight: 400; letter-spacing: 1px; line-height: 1; }
  .name-block__last { font-size: 22px; font-weight: 300; line-height: 1.2; }
  .name-block__divider { display: flex; align-items: center; gap: 6px; margin: 4px 0 3px; }
  .name-block__divider span { height: 1.5px; width: 42px; background: var(--ink); }
  .name-block__divider svg { width: 9px; height: 9px; }
  .name-block__title { font-size: 12px; letter-spacing: 1px; }

  .rule { width: 3px; height: 170px; background: var(--ink); flex: none; }

  .phone { font-size: 40px; font-weight: 300; line-height: .92; letter-spacing: 1px; flex: none; }

  .contact { font-size: 13px; line-height: 1.25; letter-spacing: .5px; white-space: nowrap; }
  .contact__label { font-weight: 600; }
</style>
</head>
<body>
<main class="stage">
  <section class="card card--front" aria-label="Card front">
    <p class="front__company">Swiftgate Portals Pty. Ltd.</p>
    <div class="front__logo-box"><p class="front__logo-text">your<br>logo?</p></div>
    <p class="front__brand-line">Varnel Corvista High Speed Doors</p>
  </section>

  <section class="card card--back" aria-label="Card back">
    <div class="back__layout">
      <div class="name-block">
        <p class="name-block__first">GORDON</p>
        <p class="name-block__last">T. Halloway</p>
        <div class="name-block__divider">
          <span></span>
          <svg viewBox="0 0 10 10" aria-hidden="true"><polygon points="5,0 6.2,3.6 10,3.7 7,6 8.1,9.7 5,7.5 1.9,9.7 3,6 0,3.7 3.8,3.6" fill="#111"/></svg>
          <span></span>
        </div>
        <p class="name-block__title">SALES MANAGER</p>
      </div>
      <div class="rule"></div>
      <p class="phone">+0<br>491<br>538<br>260</p>
      <div class="rule"></div>
      <div class="contact">
        <p class="contact__label">SALES@</p>
        <p>swiftgateportals.com.au</p>
        <p class="contact__label">WEBSITE</p>
        <p>swiftgateportals.com.au</p>
      </div>
    </div>
  </section>
</main>
</body>
</html>
```